Business Card Design for New Game Studio

We need a business card design. We are a new company developing innovative mobile and platform games.

I would like to see very innovative design thats brings out the company's goal and direction.

My Company's goal and direction is to "Evolve the way of gaming, Bring fun and entertainment to all gamers"

Please do use our company logo which I have attached to be included in the design.

Please put in details for name, title, contacts etc ... be creative !!!

Reason: Company logo redesign. Awaiting it. Thanks

Hi all Please do wait for my updated company logo. Thanks

Reason: Still waiting on new company logo. Thanks all

Hi All Designers .... Sorry for the long wait... Please see the new file for my new company logo uploaded. Waiting to see all your creative design. Cheers

Hi All .... Please do not just mass send a whole bunch of similar designs .... Would like to see quality instead of quantity Cheers

Entertainment

```html
<!DOCTYPE html>
<html lang="en">
<head>
<meta charset="utf-8">
<title>Lumora Games – Business Card</title>
<link rel="stylesheet" href="https://fonts.googleapis.com/css2?family=Aldrich&display=swap">
<style>
  :root {
    --backdrop: #3a3a3a;
    --card-black: #050505;
    --lime: #d4e021;
    --ink-light: #f2f2f2;
    --ink-muted: #cfcfcf;
  }
  * { margin: 0; padding: 0; box-sizing: border-box; }
  html, body {
    width: 1200px;
    height: 900px;
    overflow: hidden;
    background: var(--backdrop);
    font-family: "Aldrich", sans-serif;
  }
  .card {
    position: absolute;
    width: 520px;
    height: 300px;
    background: var(--card-black);
    overflow: hidden;
    box-shadow: 0 12px 30px rgba(0,0,0,0.45);
  }
  .card--front { left: 50px; top: 330px; }
  .card--back  { left: 630px; top: 270px; }
  .card__wave {
    position: absolute;
    inset: 0;
    width: 100%;
    height: 100%;
  }
  .wave__fill { fill: var(--lime); }
  .wave__line { fill: none; stroke: var(--lime); stroke-width: 1.4; }

  .identity {
    position: absolute;
    left: 34px;
    top: 196px;
    color: var(--ink-light);
  }
  .identity__company {
    font-size: 22px;
    font-variant: small-caps;
    letter-spacing: 0.5px;
  }
  .identity__title {
    margin-top: 4px;
    margin-left: 36px;
    font-size: 13px;
    color: var(--ink-muted);
  }
  .brand {
    position: absolute;
    right: 30px;
    bottom: 28px;
    display: flex;
    align-items: center;
    gap: 10px;
    color: var(--lime);
    font-size: 26px;
  }
  .brand__square {
    width: 22px;
    height: 22px;
    background: var(--lime);
  }

  .tagline {
    position: absolute;
    right: 40px;
    top: 150px;
    text-align: right;
    color: var(--ink-light);
    font-variant: small-caps;
    line-height: 1.5;
  }
  .tagline__lead { font-size: 15px; letter-spacing: 1px; }
  .tagline__sub { font-size: 13px; letter-spacing: 0.6px; }

  .contacts {
    position: absolute;
    left: 130px;
    top: 212px;
    list-style: none;
    color: var(--ink-light);
    font-size: 13px;
    line-height: 1.55;
  }
  .contacts__item {
    display: flex;
    align-items: center;
    justify-content: space-between;
    width: 150px;
  }
  .contacts__icon {
    width: 11px;
    height: 11px;
    fill: none;
    stroke: var(--ink-light);
    stroke-width: 1.4;
  }
</style>
</head>
<body>

<section class="card card--front" aria-label="Business card front">
  <svg class="card__wave" viewBox="0 0 520 300" aria-hidden="true">
    <path class="wave__fill" d="M0 0 H520 V230 C505 200 480 165 430 150 C330 118 180 110 0 118 Z"/>
    <path class="wave__line" d="M0 128 C180 120 330 128 430 160 C475 175 500 205 512 240"/>
    <path class="wave__line" d="M0 134 C180 126 330 134 425 166 C468 181 492 212 502 248"/>
  </svg>
  <div class="identity">
    <p class="identity__company">Company name</p>
    <p class="identity__title">Title</p>
  </div>
  <div class="brand">
    <span class="brand__square"></span>
    <span class="brand__name">Lumora Games</span>
  </div>
</section>

<section class="card card--back" aria-label="Business card back">
  <svg class="card__wave" viewBox="0 0 520 300" aria-hidden="true">
    <path class="wave__fill" d="M0 0 H520 V150 C505 125 480 105 430 98 C330 82 180 80 0 82 Z"/>
    <path class="wave__line" d="M0 92 C180 90 330 92 430 108 C475 116 500 132 512 155"/>
    <path class="wave__line" d="M0 98 C180 96 330 98 425 114 C468 122 492 138 502 162"/>
  </svg>
  <div class="tagline">
    <p class="tagline__lead">Evolve the way of gaming</p>
    <p class="tagline__sub">Bring fun and entertainment to all gamers</p>
  </div>
  <ul class="contacts">
    <li class="contacts__item">www.website.com
      <svg class="contacts__icon" viewBox="0 0 12 12"><circle cx="6" cy="6" r="5"/><path d="M1 6 H11 M6 1 C3 4 3 8 6 11 M6 1 C9 4 9 8 6 11"/></svg>
    </li>
    <li class="contacts__item">Your Email.com
      <svg class="contacts__icon" viewBox="0 0 12 12"><rect x="1" y="2.5" width="10" height="7"/><path d="M1 2.5 L6 7 L11 2.5"/></svg>
    </li>
    <li class="contacts__item">Your Phone
      <svg class="contacts__icon" viewBox="0 0 12 12"><rect x="3" y="1" width="6" height="10" rx="1"/><path d="M5 9 H7"/></svg>
    </li>
  </ul>
</section>

</body>
</html>
```